Aircraft maintenance buisness card

I am an aircraft mechanic looking for a personal buisness card . I would like my name and a title of Aircraft Maintenance Manager . I would like a suttle picture of an aircraft and helicopter .

elegant and professional wtih my contact .

My name should be on the car and Aircraft Maintenance Manager under with my contact infor below .

i have attached some pictures but i am open to other pics and ideas . I would like a airliner or private jet and a helicopter in the picture . The Images should be suttle and not the main idea . I also uploaded a picture of a jet engine which is cool . Be creative and i will work with you to finalize something .
Updates

Project Deadline Extended
Reason: Looking for more variations . Very good so far but looiking for a bit more styles and i uploaded my logo that i purchased . Please use my logo and be creative with it . I like some variations of black card with maybe some pictures that i uploaded but i am open to ideas . Be creative and i will work with you .

Project Deadline Extended
Reason: Looking for more designs and variations . Not yet satisfied with the designs i have gotten .

Industry/Entity Type

Aviation

Contact Information for Business Card

Aircraft Maintenance Manager

Font styles to use
Serif

Colors

Designer to choose colors to be used in the design.

Requirements
Must have
• An aviation related Logo if possible incorporated in the card possibly
• My name
• Tiberio Malvade Furtunato
• 482 Pellow St.
• Brenmoor , DE
• 08519
• Email: Lwskyfixtech@mailvora.com
Nice to have
• Suttle Backround of a Private Jet or Airliner and a Helicopter .

```html
<!DOCTYPE html>
<html lang="en">
<head>
<meta charset="utf-8">
<title>Skyfix Aviation – Business Card</title>
<link rel="stylesheet" href="https://fonts.googleapis.com/css2?family=Poppins:wght@400;500;700&display=swap">
<style>
  :root {
    --canvas: #e6e6e8;
    --card-light: #efeff1;
    --ink: #1b1b1d;
    --ink-soft: #2a2a2e;
    --accent-blue: #1f48a8;
    --logo-white: #ffffff;
  }
  * { box-sizing: border-box; margin: 0; padding: 0; }
  html, body {
    width: 1200px;
    height: 1000px;
    overflow: hidden;
    background: var(--canvas);
    font-family: "Poppins", sans-serif;
  }
  .canvas { position: relative; width: 1200px; height: 1000px; }
  .card {
    position: absolute;
    width: 592px;
    height: 338px;
    overflow: hidden;
  }
  .card-front { left: 304px; top: 130px; background: var(--card-light); }
  .card-back { left: 304px; top: 532px; }

  .card-art { position: absolute; inset: 0; width: 592px; height: 338px; }

  .contact-list {
    position: absolute;
    left: 32px;
    top: 100px;
    list-style: none;
    color: var(--ink);
    font-size: 16.5px;
    line-height: 19px;
  }
  .contact-item { display: flex; align-items: flex-start; gap: 14px; }
  .contact-item + .contact-item { margin-top: 24px; }
  .contact-icon { flex: none; width: 22px; height: 32px; }
  .contact-icon.mail { height: 20px; margin-top: 1px; }

  .identity { position: absolute; left: 30px; top: 264px; }
  .identity-name {
    font-weight: 700;
    font-size: 25.5px;
    line-height: 30px;
    color: var(--ink);
  }
  .identity-title {
    font-weight: 400;
    font-size: 16px;
    line-height: 20px;
    color: var(--accent-blue);
  }

  .brand {
    position: absolute;
    display: flex;
    align-items: center;
    color: var(--logo-white);
    font-family: "Poppins", sans-serif;
    font-weight: 700;
  }
  .brand-dot { border: 3px solid var(--logo-white); border-radius: 50%; flex: none; }
  .brand-front { left: 418px; top: 112px; gap: 9px; font-size: 16px; line-height: 20px; }
  .brand-front .brand-dot { width: 44px; height: 44px; }
  .brand-front .brand-name { width: 80px; }
  .brand-back { left: 190px; top: 124px; gap: 16px; font-size: 30px; line-height: 34px; }
  .brand-back .brand-dot { width: 96px; height: 96px; border-width: 5px; }
  .brand-back .brand-name { width: 160px; }
</style>
</head>
<body>
<main class="canvas">

  <section class="card card-front" aria-label="Business card front">
    <svg class="card-art" viewBox="0 0 592 338">
      <defs>
        <linearGradient id="hangarTone" x1="0" y1="0" x2="0" y2="1">
          <stop offset="0" stop-color="#15181d"/>
          <stop offset="0.45" stop-color="#27303d"/>
          <stop offset="1" stop-color="#3b4a5e"/>
        </linearGradient>
      </defs>
      <polygon role="img" aria-label="Photo of an aircraft propeller under a glass hangar roof"
               points="250,0 592,0 592,338 512,338 440,262 410,256 345,190"
               fill="url(#hangarTone)"/>
      <polygon class="stripe" points="222,0 240,0 350,190 334,190" fill="var(--accent-blue)"/>
      <polygon class="stripe" points="252,0 262,0 336,108 326,108" fill="var(--accent-blue)"/>
      <polygon class="stripe" points="520,0 532,0 592,92 592,110" fill="var(--accent-blue)"/>
      <polygon class="stripe" points="424,262 446,262 522,338 500,338" fill="var(--accent-blue)"/>
    </svg>

    <ul class="contact-list">
      <li class="contact-item">
        <svg class="contact-icon pin" viewBox="0 0 22 32" aria-hidden="true">
          <path d="M11 1C5.5 1 1.5 5.2 1.5 10.5 1.5 17.5 11 30 11 30s9.5-12.5 9.5-19.5C20.5 5.2 16.5 1 11 1z"
                fill="none" stroke="var(--ink-soft)" stroke-width="2.6"/>
          <circle cx="11" cy="10.5" r="3.4" fill="var(--ink-soft)"/>
        </svg>
        <span class="contact-text">482 Pellow St.<br>Brenmoor , DE&nbsp; 08519</span>
      </li>
      <li class="contact-item">
        <svg class="contact-icon mail" viewBox="0 0 22 18" aria-hidden="true">
          <rect x="1.2" y="1.2" width="19.6" height="15.6" fill="none" stroke="var(--ink-soft)" stroke-width="2"/>
          <path d="M1.5 1.8 11 10 20.5 1.8M1.5 16.5l7-6.5M20.5 16.5l-7-6.5" fill="none" stroke="var(--ink-soft)" stroke-width="1.8"/>
        </svg>
        <span class="contact-text">Lwskyfixtech@mailvora.com</span>
      </li>
    </ul>

    <div class="identity">
      <h1 class="identity-name">Tiberio Malvade Furtunato</h1>
      <p class="identity-title">Aircraft Maintenance Manager</p>
    </div>

    <div class="brand brand-front">
      <span class="brand-dot"></span>
      <span class="brand-name">SKYFIX AVIATION</span>
    </div>
  </section>

  <section class="card card-back" aria-label="Business card back">
    <svg class="card-art" viewBox="0 0 592 338">
      <defs>
        <linearGradient id="hangarToneBack" x1="0" y1="0" x2="0" y2="1">
          <stop offset="0" stop-color="#111418"/>
          <stop offset="0.5" stop-color="#232b36"/>
          <stop offset="1" stop-color="#34425a"/>
        </linearGradient>
      </defs>
      <rect role="img" aria-label="Photo of an aircraft propeller under a glass hangar roof with sky behind"
            width="592" height="338" fill="url(#hangarToneBack)"/>
    </svg>

    <div class="brand brand-back">
      <span class="brand-dot"></span>
      <span class="brand-name">SKYFIX AVIATION</span>
    </div>
  </section>

</main>
</body>
</html>
```